" Nós fazemos a administração geral dos condomínios. O que envolve solução de conflitos, contratação de serviços, orçamentos, administração financeira, reuniões de condôminos, relatórios gerenciais, orientações diversas ao síndico, conselheiros e condôminos. "

```html
<!DOCTYPE html>
<html lang="pt-BR">
<head>
<meta charset="UTF-8">
<title>Alvorada – Papel timbrado</title>
<link href="https://fonts.googleapis.com/css2?family=Montserrat:wght@400;600;700&display=swap" rel="stylesheet">
<style>
  :root {
    --backdrop: #e9eaec;
    --paper: #ffffff;
    --navy: #1b3556;
    --sky: #2aa3d8;
    --ink: #26384f;
  }
  * { margin: 0; padding: 0; box-sizing: border-box; }
  html, body {
    width: 1200px; height: 1200px; overflow: hidden;
    background: var(--backdrop);
    font-family: "Montserrat", sans-serif;
  }
  .letterhead {
    position: absolute;
    left: 190px; top: 20px;
    width: 820px; height: 1160px;
    background: var(--paper);
  }
  .brand {
    position: absolute;
    top: 78px; left: 459px;
    transform: translateX(-50%);
    display: flex; align-items: center; gap: 14px;
  }
  .brand-square {
    width: 22px; height: 22px;
    background: var(--sky);
  }
  .brand-name {
    font-weight: 700;
    font-size: 34px;
    letter-spacing: 1px;
    color: var(--navy);
  }
  .footer-rule {
    position: absolute;
    left: 10px; right: 10px; top: 1082px;
    height: 6px;
    background: var(--navy);
  }
  .footer {
    position: absolute;
    left: 22px; right: 10px; top: 1106px;
    display: flex; justify-content: space-between;
    font-size: 14px; line-height: 1.45;
    color: var(--ink);
  }
  .footer-address { width: 380px; }
  .footer-phones { width: 220px; }
  .footer-email { text-align: right; }
</style>
</head>
<body>
  <main class="letterhead">
    <header class="brand">
      <span class="brand-square"></span>
      <span class="brand-name">ALVORADA</span>
    </header>

    <div class="footer-rule"></div>
    <footer class="footer">
      <p class="footer-address">Rua das Acácias, 120, Sala 210<br>Cotia, SP, CEP 06700-000</p>
      <p class="footer-phones">(11) 4000-1234<br>(11) 9 0000-5678</p>
      <p class="footer-email">contato@alvoradaadm.com.br</p>
    </footer>
  </main>
</body>
</html>
```